Business cards to launch an education platform

Hi,
I am looking at having new business cards designed.
I am a startup, developing a web platform for schools and university, the education world. It's an online assessment system.
I would like a card that looks classy, and that is using the colors and the font of my logo.

I have attached:
1) my logo
2) A business card that I have designed quickly so you can have all the information required in the card, but I really don't like it.
3) The font that I am using (Lato Regular) to design my web platform
4) Some screenshots of my web platform so you can have a look at the style that I have.

Target Market(s)

Major market: Education system: Schools and university
Minor markets: Business in general

Industry/Entity Type

Business

Contact Information for Business Card

Lydia Marsh
Director

M: 0437 681 902
E: lydia.marsh@copperLeafSystems.com.au

Requirements
Must have
• The colors of my logo

```html
<!DOCTYPE html>
<html lang="en">
<head>
<meta charset="utf-8">
<title>Copper Leaf Systems – Business Card</title>
<link rel="stylesheet" href="https://fonts.googleapis.com/css2?family=Lato:wght@400;700&display=swap">
<style>
  :root {
    --backdrop: #2b201d;
    --card-white: #ffffff;
    --navy: #0b3f72;
    --ink: #14325a;
    --mid-blue: #1a88cc;
    --sky-blue: #29b3e6;
    --mist-grey: #cfd8e2;
  }
  * { margin: 0; padding: 0; box-sizing: border-box; }
  html, body {
    width: 1200px; height: 999px; overflow: hidden;
    background: var(--backdrop);
    font-family: "Lato", sans-serif;
  }
  .sheet {
    position: relative; width: 1200px; height: 999px;
    display: flex; align-items: center; justify-content: center; gap: 60px;
  }
  .card {
    position: relative; width: 520px; height: 318px;
    background: var(--card-white);
    border-radius: 22px; overflow: hidden;
    box-shadow: 0 16px 36px rgba(0,0,0,0.45);
  }
  .card-shapes { position: absolute; inset: 0; width: 100%; height: 100%; }
  .brand {
    position: absolute; display: flex; align-items: center; gap: 10px;
    color: var(--navy); font-weight: 700; letter-spacing: 0.5px; white-space: nowrap;
  }
  .brand-mark { background: var(--mid-blue); }
  .card-front .brand { left: 70px; top: 40px; font-size: 20px; }
  .card-front .brand-mark { width: 18px; height: 18px; }
  .card-back .brand { left: 50%; top: 50%; transform: translate(-50%, -50%); font-size: 30px; }
  .card-back .brand-mark { width: 28px; height: 28px; }
  .person {
    position: absolute; right: 28px; top: 112px; text-align: right; color: var(--card-white);
    white-space: nowrap;
  }
  .person-name { font-size: 26px; font-weight: 400; letter-spacing: 1px; text-transform: uppercase; }
  .person-role { font-size: 18px; margin-top: 2px; }
  .contact {
    position: absolute; right: 24px; display: flex; align-items: center; gap: 10px;
    color: var(--ink); white-space: nowrap;
  }
  .contact-email { top: 208px; font-size: 14px; }
  .contact-phone { top: 250px; font-size: 22px; letter-spacing: 0.5px; }
  .contact-icon { width: 28px; height: 28px; flex: none; }
</style>
</head>
<body>
<main class="sheet">

  <section class="card card-front">
    <svg class="card-shapes" viewBox="0 0 520 318" aria-hidden="true">
      <polygon points="0,105 36,92 0,128" fill="var(--sky-blue)"/>
      <polygon points="0,128 36,92 170,318 120,318" fill="var(--mist-grey)"/>
      <polygon points="0,128 120,318 0,318" fill="var(--navy)"/>
      <polygon points="240,0 520,0 520,190 310,190" fill="var(--mid-blue)"/>
      <polygon points="470,318 520,240 520,278 495,318" fill="var(--mist-grey)"/>
      <polygon points="495,318 520,278 520,318" fill="var(--sky-blue)"/>
    </svg>
    <div class="brand"><span class="brand-mark"></span>Copper Leaf Systems</div>
    <div class="person">
      <div class="person-name">Lydia Marsh</div>
      <div class="person-role">Director</div>
    </div>
    <div class="contact contact-email">
      <span>lydia.marsh@copperLeafSystems.com.au</span>
      <svg class="contact-icon" viewBox="0 0 28 28" aria-label="Email">
        <circle cx="14" cy="14" r="14" fill="var(--sky-blue)"/>
        <rect x="7" y="9" width="14" height="10" fill="none" stroke="#fff" stroke-width="1.6"/>
        <polyline points="7,9 14,15 21,9" fill="none" stroke="#fff" stroke-width="1.6"/>
      </svg>
    </div>
    <div class="contact contact-phone">
      <span>0437 681 902</span>
      <svg class="contact-icon" viewBox="0 0 28 28" aria-label="Phone">
        <circle cx="14" cy="14" r="14" fill="var(--ink)"/>
        <path d="M9 8 q-2 2 0 6 q3 5 8 7 q3 1 4-1 l-2.5-2.5 q-1 1-2 0.5 q-3-1.5-4.5-4.5 q-0.5-1 0.5-2 z" fill="#fff"/>
      </svg>
    </div>
  </section>

  <section class="card card-back">
    <svg class="card-shapes" viewBox="0 0 520 318" aria-hidden="true">
      <polygon points="0,60 42,45 0,95" fill="var(--sky-blue)"/>
      <polygon points="0,95 42,45 160,318 115,318" fill="var(--mist-grey)"/>
      <polygon points="0,95 115,318 0,318" fill="var(--navy)"/>
      <polygon points="330,0 520,0 520,230" fill="var(--mid-blue)"/>
      <polygon points="300,0 330,0 520,230 520,275" fill="var(--mist-grey)"/>
      <polygon points="430,318 520,250 520,318" fill="var(--sky-blue)"/>
    </svg>
    <div class="brand"><span class="brand-mark"></span>Copper Leaf Systems</div>
  </section>

</main>
</body>
</html>
```